Redesign existing website

We would like a redesign of the website http://www.velbrisanalytics.com that creates a more modern, up to date look.

Velbris Analytics creates software for social science research and is focused on making the software user friendly and easy to use. We would like to convey seriousness, but also
a very up to date, just released look.

Feel free to modify the logo if you wish.

Target Market(s)

Academics, researchers

Industry/Entity Type

Software

Requirements
Must have
• The design should incorporate the same information as the current website.

```html
<!DOCTYPE html>
<html lang="en">
<head>
<meta charset="utf-8">
<title>Velbris Analytics</title>
<link href="https://fonts.googleapis.com/css2?family=Pathway+Gothic+One&family=Open+Sans:wght@400&display=swap" rel="stylesheet">
<style>
:root{
  --page-bg:#ececec;
  --sheet:#ffffff;
  --ink:#222222;
  --text:#333333;
  --muted:#555555;
  --brand:#1f3f8f;
  --line:#d6d6d6;
  --panel:#f2f2f2;
  --panel-border:#cfcfcf;
  --nav-top:#f4f4f4;
  --nav-bottom:#cdcdcd;
  --hero-top:#1a4db8;
  --hero-mid:#3f86e6;
  --hero-bottom:#9fe3fb;
  --date:#1f3fa0;
}
*{margin:0;padding:0;box-sizing:border-box}
html,body{width:1081px;height:1200px;overflow:hidden;background:var(--page-bg)}
body{position:relative;font-family:"Pathway Gothic One",sans-serif;color:var(--text)}
.sheet{position:absolute;left:95px;top:0;width:886px;height:1200px;background:var(--sheet);border-left:1px solid var(--line);border-right:1px solid var(--line)}
.abs{position:absolute}
.brand{left:110px;top:12px;display:flex;align-items:center;gap:10px;height:92px}
.brand-dot{width:22px;height:22px;border-radius:50%;background:var(--brand)}
.brand-name{font-size:30px;color:var(--brand);letter-spacing:.5px}
.social{left:866px;top:21px;display:flex;gap:3px}
.social span{width:20px;height:20px;border-radius:3px;background:#8a9bb8}
.search{left:740px;top:79px;width:196px;height:25px;border:1px solid #c8c8c8;border-radius:4px;background:#fafafa}
.search-btn{left:943px;top:81px;width:22px;height:22px}
.nav{left:108px;top:124px;width:863px;height:42px;background:linear-gradient(var(--nav-top),var(--nav-bottom));border-radius:3px;box-shadow:0 1px 2px rgba(0,0,0,.2)}
.nav a{position:absolute;top:10px;font-size:19px;color:var(--ink);text-decoration:none}
.hero{left:108px;top:168px;width:863px;height:330px;background:linear-gradient(var(--hero-top),var(--hero-mid) 55%,var(--hero-bottom))}
.product-box{left:190px;top:185px;width:222px;height:317px;background:linear-gradient(90deg,#1b1b1b,#3a3a3a 60%,#4f7fe0);border-radius:2px}
.hero-title{left:470px;top:226px;width:420px;text-align:center;font-size:39px;line-height:39px;color:#fff;text-shadow:0 2px 3px rgba(0,0,0,.45)}
.btn{height:52px;top:385px;background:linear-gradient(#fafafa,#d2d2d2);box-shadow:0 1px 3px rgba(0,0,0,.35);font-size:20px;color:var(--ink);display:flex;align-items:center;justify-content:center}
h2{position:absolute;font-weight:400;font-size:32px;color:var(--ink)}
.copy{font-size:14.5px;line-height:15.3px;color:var(--text)}
.copy p{margin-bottom:15px}
.panel{top:811px;height:252px;background:var(--panel);border:1px solid var(--panel-border)}
.item{position:absolute;left:10px;right:10px}
.item h3{font-weight:400;font-size:18px;line-height:18px;color:var(--ink);margin-bottom:8px}
.item p{font-family:"Open Sans",sans-serif;font-size:11px;line-height:12.7px;color:var(--muted)}
.item .date{text-align:right;color:var(--date);margin-top:5px}
.field{position:absolute;left:85px;width:131px;height:29px;background:#fff;border:1px solid #c8c8c8}
.label{position:absolute;left:13px;font-size:15px;color:var(--ink)}
.signin{left:62px;top:188px;width:86px;height:32px;background:linear-gradient(#8a8a8a,#4e4e4e);color:#fff;font-size:19px;display:flex;align-items:center;justify-content:center}
.footer-rule{left:95px;top:1124px;width:886px;height:1px;background:var(--line)}
.footer-nav{left:95px;top:1140px;width:886px;text-align:center;font-size:15px;color:var(--muted)}
.footer-nav span{margin:0 9px}
.copyright{left:95px;top:1163px;width:886px;text-align:center;font-size:15px;color:var(--muted)}
</style>
</head>
<body>
<div class="sheet"></div>

<header>
  <div class="abs brand"><span class="brand-dot"></span><span class="brand-name">Velbris Analytics</span></div>
  <div class="abs social"><span></span><span></span><span></span><span></span></div>
  <div class="abs search"></div>
  <svg class="abs search-btn" viewBox="0 0 22 22"><circle cx="11" cy="11" r="10" fill="#f4f4f4" stroke="#ccc"/><circle cx="9.5" cy="9.5" r="3.5" fill="none" stroke="#333" stroke-width="1.6"/><line x1="12" y1="12" x2="16" y2="15" stroke="#333" stroke-width="2"/></svg>
  <nav class="abs nav">
    <a style="left:22px">Home</a><a style="left:99px">Products</a><a style="left:194px">Features</a><a style="left:288px">News</a><a style="left:371px">About us</a><a style="left:465px">Support</a><a style="left:567px">Download</a><a style="left:672px">Contact us</a>
  </nav>
</header>

<section>
  <div class="abs hero"></div>
  <div class="abs product-box" role="img" aria-label="Software box for Velbris Data Manager"></div>
  <div class="abs hero-title">Increasing the power and efficiency of empirical social science research</div>
  <div class="abs btn" style="left:497px;width:203px">Preview Release Available!</div>
  <div class="abs btn" style="left:711px;width:202px">Download Preview Release</div>
</section>

<section>
  <h2 style="left:114px;top:528px">Who we are?</h2>
  <div class="abs copy" style="left:116px;top:584px;width:460px">
    <p>The mission of Velbris Analytics, Inc. is to produce software products that multiply the power and efficiency of empirical scientific research in the social sciences.</p>
    <p>A central goal is to expand access to complex data sources and to the advanced methods of scientific investigation needed to analyze them. The mission of Velbris Analytics, Inc. is to produce software products that multiply the power and efficiency of empirical scientific research in the social sciences.</p>
    <p>A central goal is to expand access to complex data sources and to the advanced methods of scientific investigation needed to analyze them.</p>
  </div>
  <h2 style="left:616px;top:528px">What we do?</h2>
  <div class="abs copy" style="left:618px;top:584px;width:345px">
    <p>The mission of Velbris Analytics, Inc. is to produce software products that multiply the power and efficiency of empirical scientific research in the social sciences.</p>
    <p>A central goal is to expand access to complex data sources and to the advanced methods of scientific investigation needed to analyze them. The mission of Velbris Analytics, Inc. is to produce software products that multiply the power and efficiency of empirical scientific research in on of Velbris Analytics the social sciences analyze them.</p>
  </div>
</section>

<section>
  <h2 style="left:114px;top:772px">Our Products</h2>
  <div class="abs panel" style="left:116px;width:293px">
    <div class="item" style="top:20px"><h3>Social Science and Health Data Management</h3><p>The technology used for retrieving and manipulating data has remained virtually unchanged since the first statistical packages were introduced almost four decades ago...</p></div>
    <div class="item" style="top:130px"><h3>The Velbris Data Manager Architecture</h3><p>The technology used for retrieving and manipulating data has remained virtually unchanged since the first statistical packages were introduced almost four decades ago...</p></div>
  </div>

  <h2 style="left:423px;top:772px">Latest News</h2>
  <div class="abs panel" style="left:423px;width:293px">
    <div class="item" style="top:19px"><h3>An early access preview of the Velbris Data Manager is available.</h3><p>The technology used for retrieving and manipulating data has remained virtually unchanged since the first statistical ...</p><p class="date">April, 2009</p></div>
    <div class="item" style="top:136px"><h3>The Velbris Data Manager Architecture</h3><p>The technology used for retrieving and manipulating data has remained virtually unchanged since the first statistical packages...</p><p class="date">April, 2009</p></div>
  </div>

  <h2 style="left:732px;top:772px">Login</h2>
  <form class="abs panel" style="left:732px;width:233px">
    <span class="label" style="top:36px">User Name</span><span class="field" style="top:29px"></span>
    <span class="label" style="top:76px">Password</span><span class="field" style="top:70px"></span>
    <span class="abs" style="left:88px;top:118px;font-size:14px;color:var(--muted)">Forget Password?</span>
    <span class="abs" style="left:88px;top:148px;width:12px;height:12px;border:1px solid #bbb;background:#fff"></span>
    <span class="abs" style="left:108px;top:145px;font-size:14px;color:var(--muted)">Remember me</span>
    <div class="abs signin">Sign in</div>
  </form>
</section>

<footer>
  <div class="abs footer-rule"></div>
  <div class="abs footer-nav"><span>Home</span><span>Products</span><span>Features</span><span>News</span><span>About us</span><span>Support</span><span>Download</span><span>Contact us</span></div>
  <div class="abs copyright">Copyright @ 2011 Velbrisanalytics.com</div>
</footer>
</body>
</html>
```